Ferrobay | Minimalist 6-panel Brochure

Background: Ferro Bay Fabricators Corp. is a manufacturer of steel wire-based products (e.g. nails, galvanized wire, barbed wire, steel matting) in Manila.

Brand Differentiator: Uncompromising "first world" quality to push our "third world" country to develop

Customers: We are a B2B company - we supply the materials to be used by Contractors in building projects. Retailers in selling to home users,Wholesalers in distributing to their retailer networks.

Brochure Objective: Using a standard 6-panel 8.5" x 11" Brochure, to create awareness among contractors and in the architectural community as a leader in quality products and honest service. (architects are big influencers of contractors in that they can recommend quality suppliers to them)

Brochure Contents: I have attached (in Powerpoint) the copy points of the Brochures broken down by 6 panels of content.
**DO NOT MIND how I've layout-ed the info in the .ppt, It's for your easier understanding only**

Brand Essence to Consider: 'First-world' in terms of product standards. Transparent & honest in terms of service/delivery. Approachable from Big to Small customers.

*Bonus Brand Essence: Someone you can have a 'light' conversation with over the phone for a quotation.*

Design Guidelines:
1) Be creative. If you think any of the guidelines I mention below won't be the best fit to your interpretation of my vision, go ahead and do what you think is best!

2) Be minimalist. I've kept the copy points's words at a minimum so there would be more emphasis on the content. Design around the copy points that bring out the gist more and the details less.

3) Design flat. Make the design look simple yet attractive.
PEG: If there was a website that I'd like to take design cues from, it's www.plinthory.com and tovelink.com/purse . Details like font size, font color, etc here were nicely differentiated for Headers, Subtexts and Descriptions. Be playful with using font effects like BOLD and Italics.

4) Use Icons. Instead of using a photo-heavy brochure, it would be better if we created icons for the brochure parts ('Our Thinking', 'How We Serve You', 'How It Works')
PEG: Abstract/minimalist icons such as those seen at the top of quellmarks.com or the middle section of inkvardle.com would be nice.

5) Edit the Product Shots and Pics of our Tech/Machines. Kindly edit and 'beautify' the photos attached to align to your design. Use 1 shot per product. Some are in .jpeg and some in .psd. (see attached. remove the watermarks in .psd shots)

6) Fit the Logo. Feel free to change to color schemes of our logo to make it fit with your designs. (see attached)

7) Front Cover. Kindly go through our 'Tagline' and 'Short Overall Description' first to find inspiration for some simple artwork.
*sidenote: For you to understand our tagline, the Philippines hasn't fully developed a priority for quality in terms of steel materials used in construction. (price had always dictated the market) And we want to help push them to that point in shaping the country's real estate development from 3rd world to a 1st world country's standards.

8) Word Cloud. I've listed 8 of the biggest and well-known projects we've supported in the past 5 years in 'Supported Projects' and my idea is for you to create a nice 'Word Cloud' of it similar to how I presented it in the ppt attached. Or it can be presented in some shape you'd think is nice. (search "word cloud" in Zendro Pictures)

9) Call-to-Action. Make the 'Call-to-Action' panel of the brochure as "inviting" as possible.

10) Be creative. AGAIN. Aside for the copy points in the ppt guidelines attached, I would like to stress that you are free to edit/create whatever you deem fit to my vision. (as you've come to know what I'd like by now)

Don't forget to have fun!! It'll be awesome working with you.

**UPDATE in July 24: Use the PPT v2 for details, attached separately. (now with design pegs)**

**UPDATE in July 29: for the photos under 'First World Tech', please use the Cutter photo and Wire-drawing machine photo attached here.**
Updates

Hello again! Good job so far on the initial designs. To let you know what style I'd like our icons in "How We Serve You", please visit www.ferrobayph.sitevane.com for our mock-up website.

You can also scroll down in the first page in "Our 4 Products" to see how I'd like our fonts to be used here so it'll be readable (i.e. through different font sizes, font effects like Bold & Italic)

As always, if you think you have a better idea on how to execute what I've mentioned above, go do it!

**UPDATE in July 24: Use the PPT v2 for the copy details, attached separately. Now with Design PEGS.**

Reason: extending for a few more days for last-minute submissions/revisions. Thanks!

Target Market(s)

Architectural firms. Building contractors. Steel wholesalers/distributors.

Industry/Entity Type

Real Estate

Requirements
Must have
• Simple. Approachable. Clear. Attractive. Uncluttered.
Should not have
• BULLET POINTS. (this shouldn't look like a Powerpoint material in any way or form)

```html
<!DOCTYPE html>
<html lang="en">
<head>
<meta charset="utf-8">
<title>Ferrobay Brochure</title>
<link rel="stylesheet" href="https://fonts.googleapis.com/css2?family=Arimo:wght@400;700&family=Open+Sans:wght@300;400;600&family=Roboto+Condensed:ital,wght@1,700&display=swap">
<style>
  :root{
    --steel-blue:#1f5f80;
    --band-blue:#236183;
    --accent-orange:#f05a28;
    --ink:#111;
    --grey-top:#c4c4c4;
    --grey-mid:#e6e6e6;
    --paper:#fff;
  }
  *{margin:0;padding:0;box-sizing:border-box}
  html,body{width:1200px;height:922px;overflow:hidden;background:#f2f2f2}
  .brochure{position:relative;width:1200px;height:922px;display:flex}
  .panel{position:relative;width:400px;height:922px;overflow:hidden}
  .panel + .panel{border-left:1px solid #bdbdbd}
  .abs{position:absolute}

  /* testimonials panel */
  .testimonials{background:var(--paper)}
  .testimonials .title{left:0;width:400px;top:38px;text-align:center;font:italic 700 42px "Roboto Condensed",sans-serif;color:var(--steel-blue)}
  .testimonials .subhead{left:0;width:386px;top:118px;text-align:center;font:700 37px "Arimo",sans-serif;color:var(--steel-blue)}
  .accent-strip{background:var(--band-blue)}
  .photo.cutter{background:linear-gradient(135deg,#7a8470,#b9b9a9 50%,#5a5d55)}
  .photo.die{background:linear-gradient(135deg,#d8d8d8,#8d8d8d 50%,#4f4f4f)}
  .tech-band{left:0;top:515px;width:400px;height:66px;background:var(--band-blue);color:#fff;font:400 30px "Open Sans",sans-serif;padding-left:49px;line-height:66px}
  .trust-head{left:32px;top:617px;font:700 27px "Arimo",sans-serif;color:var(--steel-blue)}
  .word-cloud{left:0;top:0}
  .word-cloud text{font-family:"Open Sans",sans-serif}

  /* contact panel */
  .contact{background:linear-gradient(180deg,#f4f4f4 26%,#e9e9e9 60%,#c9c9c9 100%)}
  .contact .top-block{left:0;top:0;width:400px;height:238px;background:linear-gradient(180deg,#d6d6d6,var(--grey-top))}
  .contact .intro{left:27px;top:40px;width:360px;font:400 16.5px/29px "Open Sans",sans-serif;color:#222}
  .contact .intro p + p{margin-top:12px}
  .contact .call{left:27px;top:526px;font:400 27px "Arimo",sans-serif;color:#222}
  .contact .email{left:27px;top:570px;font:400 22px "Arimo",sans-serif;color:#222}
  .contact .web{left:27px;top:604px;font:400 20px "Arimo",sans-serif;color:#222}
  .contact .fax{left:27px;top:634px;font:400 14px "Open Sans",sans-serif;color:#222}
  .contact .about-head{left:27px;top:690px;font:700 36px "Arimo",sans-serif;color:var(--steel-blue)}
  .contact .about-copy{left:32px;top:744px;width:346px;font:400 14.5px/29px "Open Sans",sans-serif;color:#fff;text-align:justify}

  /* cover panel */
  .cover{background:var(--band-blue)}
  .cover .top-block{left:0;top:0;width:400px;height:432px;background:linear-gradient(180deg,#f7f7f7,#b9b9b9)}
  .brand{left:30px;top:38px;display:flex;align-items:center;gap:14px}
  .brand .mark{width:56px;height:56px;background:var(--steel-blue)}
  .brand .name{font:700 31px/34px "Arimo",sans-serif;color:var(--steel-blue)}
  .tagline{left:26px;top:200px;font:700 34px/44px "Arimo",sans-serif;color:var(--steel-blue)}
  .tagline .lead{font-size:48px;line-height:52px;display:block}
  .cover .white-band{left:0;top:432px;width:400px;height:127px;background:var(--paper)}
  .cover .summary{left:26px;top:448px;width:346px;font:400 14px/23px "Open Sans",sans-serif;color:#222;text-align:justify}
  .product-photo{left:0;top:559px;width:400px;height:363px;background:radial-gradient(ellipse at 80% 75%,#2a2a2a 0 30%,transparent 55%),linear-gradient(120deg,#8c9a86 0 30%,var(--band-blue) 45%,#2b5d78 100%)}
  .product-label{left:144px;top:606px;font:700 32px "Arimo",sans-serif;color:#fff}
</style>
</head>
<body>
<main class="brochure">

  <section class="panel testimonials">
    <h2 class="abs title">The Testimonials</h2>
    <h3 class="abs subhead">Technology</h3>
    <div class="abs accent-strip" style="left:0;top:234px;width:400px;height:118px"></div>
    <div class="abs photo" style="left:49px;top:185px;width:308px;height:167px;background:linear-gradient(100deg,#fff 0 8%,#2f8a5c 12% 30%,#e07b24 40% 75%,#3a6e4e 85%,#fff 95%)" role="img" aria-label="Wire-drawing machine with green and orange housings"></div>
    <div class="abs photo cutter" style="left:0;top:364px;width:183px;height:139px" role="img" aria-label="Wire cutter machine close-up"></div>
    <div class="abs photo die" style="left:195px;top:364px;width:168px;height:121px" role="img" aria-label="Wire-drawing die and pulley close-up"></div>
    <div class="abs accent-strip" style="left:363px;top:364px;width:37px;height:156px"></div>
    <div class="abs tech-band">Our First&nbsp; World Tech</div>
    <h3 class="abs trust-head">Who Trusts Our Standards</h3>
    <svg class="abs word-cloud" width="400" height="922" aria-label="Supported projects word cloud">
      <text x="98" y="724" font-size="26" fill="#111" textLength="68" lengthAdjust="spacingAndGlyphs">Varno</text>
      <text x="173" y="713" font-size="30" fill="#1f5f80" textLength="86" lengthAdjust="spacingAndGlyphs">Lumen</text>
      <text x="93" y="749" font-size="19" fill="#f05a28" textLength="140" lengthAdjust="spacingAndGlyphs">Halden’s Azalea</text>
      <text x="280" y="757" font-size="32" fill="#1f5f80" textLength="62" lengthAdjust="spacingAndGlyphs">Mall</text>
      <text x="66" y="782" font-size="22" fill="#1f5f80" textLength="102" lengthAdjust="spacingAndGlyphs">The CREST</text>
      <text x="178" y="780" font-size="30" fill="#111" textLength="138" lengthAdjust="spacingAndGlyphs">Chinatown</text>
      <text x="324" y="800" font-size="24" fill="#111" textLength="24" lengthAdjust="spacingAndGlyphs">Tr</text>
      <text x="60" y="817" font-size="32" fill="#f05a28" textLength="98" lengthAdjust="spacingAndGlyphs">Mall of</text>
      <text x="170" y="820" font-size="30" fill="#1f5f80" textLength="146" lengthAdjust="spacingAndGlyphs">The Quarry</text>
      <text x="100" y="849" font-size="24" fill="#111" textLength="128" lengthAdjust="spacingAndGlyphs">Ravel Tower</text>
      <text x="240" y="849" font-size="22" fill="#f05a28" textLength="58" lengthAdjust="spacingAndGlyphs">KLDC</text>
    </svg>
  </section>

  <section class="panel contact">
    <div class="abs top-block"></div>
    <svg class="abs" style="left:0;top:0" width="400" height="922" aria-hidden="true">
      <defs>
        <radialGradient id="glow" cx="50%" cy="80%" r="70%">
          <stop offset="0" stop-color="#fff"/>
          <stop offset="1" stop-color="#d9d9d9"/>
        </radialGradient>
      </defs>
      <circle cx="199" cy="349" r="134" fill="url(#glow)" opacity=".85"/>
    </svg>
    <div class="abs intro">
      <p>Call and give us a Hello. We’ll happily give you a quotation. E-mail is also good!<br>Got something specific in mind? Try us, we’re open to your order requests.</p>
      <p>By the way, all products are DTI-approved.</p>
    </div>
    <div class="abs call">Call: 555-0148, 5550192</div>
    <div class="abs email">ferrobaymfgcorp@mailvane.com</div>
    <div class="abs web">www.ferrobay.com.ph</div>
    <div class="abs fax">FAX # (632) 555-0173</div>
    <h2 class="abs about-head">About Company</h2>
    <p class="abs about-copy">We manufacture steel wire-based products as the construction materials used by contractors. Our aim is for every construction project be made of first world quality. We’ve done it since 1984.</p>
  </section>

  <section class="panel cover">
    <div class="abs top-block"></div>
    <svg class="abs" style="left:0;top:0" width="400" height="432" aria-hidden="true">
      <defs>
        <radialGradient id="sphere" cx="35%" cy="40%" r="65%">
          <stop offset="0" stop-color="#f2f2f2"/>
          <stop offset="1" stop-color="#a9a9a9"/>
        </radialGradient>
      </defs>
      <circle cx="445" cy="286" r="104" fill="url(#sphere)"/>
    </svg>
    <div class="abs brand">
      <span class="mark"></span>
      <span class="name">Ferrobay<br>Manufacturing</span>
    </div>
    <h1 class="abs tagline"><span class="lead">first-world</span>standards to<br>build the<br>third-world up.</h1>
    <div class="abs white-band"></div>
    <p class="abs summary">Ferrobay manufactures goods that are first world in nature &amp; truth-telling in class. Now you can build Sydney around Taguig, Shanghai inside Binondo, and Manhattan across Valero.</p>
    <div class="abs product-photo" role="img" aria-label="Gloved hands holding black annealed wire beside a wire coil"></div>
    <h2 class="abs product-label">BI Wire</h2>
  </section>

</main>
</body>
</html>
```